PRV/ Tarnwell Wood/ BSK Corporate Day - Thursday 15th May 2025

A5 Size Invitation printed front and back:
Our Company Colour is British Racing Green
INVITATION FRONT:
Background Pictures Attached:
PRV Lumber Ltd
The Quiet Harbour of Rare Grainstock
PRV Lumber/ Tarnwell Wood/ BSK Corporate Day
Thursday 15th May 2025
www.prvlumber-example.co.uk
sales@prvlumber-example.co.uk
+44 (0) 20 7946 0817
INVITATION BACK:
Golf - sponsored by Tarnwell Wood - Fennock Golf Club, Surrey
Off Road Adventure - sponsored by BSK - Address TBC
Followed by Dinner and Overnight Accommodation at
Brimwell Manor Hotel & Country Club, Surrey
We hope you will be able to join us

```html
<!DOCTYPE html>
<html lang="en">
<head>
<meta charset="utf-8">
<title>PRV Corporate Day Invitation</title>
<link rel="stylesheet" href="https://fonts.googleapis.com/css2?family=Allura&family=Bebas+Neue&family=Montserrat:wght@400;500;600;700;800;900&display=swap">
<style>
  :root{
    --page:#e2e1e2;
    --racing-green:#1f2b22;
    --olive:#4d4f1c;
    --lime:#b7d334;
    --lime-soft:#c9dc4a;
    --cream:#efe3b0;
    --script-gold:#e8d98a;
    --white:#ffffff;
    --ink:#222a22;
  }
  *{box-sizing:border-box;margin:0;padding:0}
  html,body{width:800px;height:1200px;overflow:hidden;background:var(--page)}
  body{position:relative;font-family:"Montserrat",sans-serif}

  .card{position:absolute;left:71px;width:657px;height:463px;overflow:hidden}
  .card--front{top:128px}
  .card--back{top:623px;background:var(--racing-green)}

  .photo{position:absolute;inset:0}
  .photo--course{
    background:linear-gradient(180deg,#9fb2cf 0%,#e8c3a6 22%,#f1d2ae 40%,#c7c9c4 52%,#3f5a2c 60%,#46682a 72%,#557a2d 82%,#304a20 100%);
  }
  .photo--night-course{
    background:linear-gradient(180deg,#1d2a1c 0%,#233522 30%,#1b2418 55%,#26351f 75%,#3b5524 88%,#2a3f1c 100%);
  }

  .front-title{position:absolute;inset:0;font-weight:inherit}
  .script-corporate{position:absolute;left:40px;top:24px;font-family:"Allura",cursive;font-size:76px;color:var(--ink);line-height:1;transform:rotate(-6deg);white-space:nowrap}
  .word-day{position:absolute;left:100px;top:78px;font-family:"Montserrat",sans-serif;font-weight:900;font-size:90px;color:var(--olive);line-height:1;letter-spacing:-3px;white-space:nowrap}
  .weekday{position:absolute;left:441px;top:67px;font-weight:600;font-size:17px;letter-spacing:5px;color:var(--ink);line-height:1;white-space:nowrap}
  .date-main{position:absolute;left:312px;top:85px;font-family:"Bebas Neue",sans-serif;font-size:88px;color:var(--ink);line-height:1;white-space:nowrap}
  .year{position:absolute;left:578px;top:66px;font-family:"Bebas Neue",sans-serif;font-size:50px;line-height:.88;color:var(--white)}

  .brand-mark{position:absolute;left:50px;top:318px;width:64px;display:flex;flex-direction:column;align-items:center;color:var(--white)}
  .brand-mark .dot{width:54px;height:54px;border-radius:50%;background:var(--white);margin-bottom:8px}
  .brand-mark .name{font-weight:800;font-size:24px;line-height:1}
  .brand-mark .sub{font-weight:800;font-size:6.5px;margin-top:3px;white-space:nowrap}

  /* back */
  .golf-word{position:absolute;left:36px;top:46px;font-weight:900;font-size:100px;line-height:1;color:var(--lime);letter-spacing:-3px}
  .label-sponsored{position:absolute;left:38px;top:148px;font-weight:700;font-size:17px;letter-spacing:3px;color:var(--white);line-height:1;white-space:nowrap}
  .location-tag{position:absolute;background:var(--cream);border-radius:4px;color:var(--racing-green);line-height:1;white-space:nowrap;overflow:hidden}
  .location-tag .cap{display:block;font-weight:500;letter-spacing:2px;text-transform:uppercase}
  .location-tag .place{display:block;font-weight:600}
  .location-tag--golf{left:38px;top:172px;width:184px;height:33px;padding:5px 8px}
  .location-tag--golf .cap{font-size:8px}
  .location-tag--golf .place{font-size:11.5px;margin-top:3px}
  .sponsor-badge{position:absolute;left:235px;top:144px;width:65px;height:65px;border:2px solid var(--white);border-radius:50%;display:flex;align-items:center;justify-content:center;text-align:center;color:var(--white);font-weight:700;font-size:10px;line-height:1.1}

  .divider-v{position:absolute;left:340px;top:57px;width:0;height:158px;border-left:1px dashed var(--lime)}
  .rule{position:absolute;left:359px;width:261px;height:1px;background:var(--lime)}
  .rule--top{top:58px}.rule--bottom{top:111px}

  .offroad{position:absolute;left:369px;top:69px;font-weight:900;font-size:15px;line-height:1;letter-spacing:-.4px;white-space:nowrap}
  .offroad .l1{display:block;color:var(--white)}
  .offroad .l2{display:block;color:var(--lime)}
  .offroad-sponsor{position:absolute;left:477px;top:69px;font-weight:700;font-size:7.5px;letter-spacing:1.8px;color:var(--white);line-height:1;white-space:nowrap}
  .location-tag--offroad{left:475px;top:82px;width:90px;height:20px;padding:3px 4px}
  .location-tag--offroad .cap{font-size:5.5px;letter-spacing:1px}
  .location-tag--offroad .place{font-size:7px;font-weight:700;margin-top:2px}
  .partner-name{position:absolute;left:572px;top:78px;display:flex;align-items:center;gap:4px;color:var(--white);font-weight:800;font-size:13px;line-height:1}
  .partner-name .sq{width:10px;height:10px;background:var(--white)}

  .dinner{position:absolute;left:360px;top:124px;width:258px;text-align:center;color:var(--lime-soft);font-weight:500;font-size:11.5px;letter-spacing:4.5px;line-height:14.5px;text-transform:uppercase}
  .venue{position:absolute;left:360px;top:182px;width:258px;text-align:center;color:var(--white);font-weight:500;font-size:12.5px;letter-spacing:3px;line-height:16px}

  .photo--tee{position:absolute;left:0;top:230px;width:657px;height:150px;background:radial-gradient(ellipse at 55% 40%,rgba(230,230,220,.18),rgba(0,0,0,0) 40%)}

  .closing{position:absolute;left:0;width:657px;top:366px;text-align:center;font-family:"Allura",cursive;font-size:40px;color:var(--script-gold);white-space:nowrap}
  .contacts{position:absolute;left:36px;right:36px;top:422px;display:flex;justify-content:space-between;align-items:center;color:var(--white);font-size:11px;font-weight:500}
  .contacts li{list-style:none;display:flex;align-items:center;gap:7px;white-space:nowrap}
  .contacts svg{width:11px;height:11px;fill:var(--white)}
</style>
</head>
<body>

<section class="card card--front" aria-label="Invitation front">
  <div class="photo photo--course" role="img" aria-label="Sunset view over a golf course green with bunkers and a Tudor-style clubhouse"></div>
  <h1 class="front-title">
    <span class="script-corporate">Corporate</span>
    <span class="word-day">DAY</span>
  </h1>
  <p class="weekday">THURSDAY</p>
  <p class="date-main">15TH MAY</p>
  <p class="year">20<br>25</p>
  <div class="brand-mark">
    <span class="dot"></span>
    <span class="name">PRV</span>
    <span class="sub">LUMBER LIMITED</span>
  </div>
</section>

<section class="card card--back" aria-label="Invitation back">
  <div class="photo photo--night-course" role="img" aria-label="Dusky golf course with a golf ball on a tee beside an iron club"></div>
  <div class="photo--tee" role="img" aria-label="Golf ball on a tee and iron club head on the grass"></div>

  <h2 class="golf-word">GOLF</h2>
  <p class="label-sponsored">SPONSORED BY</p>
  <div class="location-tag location-tag--golf">
    <span class="cap">Location</span>
    <span class="place">Fennock Golf Club, Surrey</span>
  </div>
  <div class="sponsor-badge">Tarnwell<br>Wood</div>

  <div class="divider-v"></div>
  <div class="rule rule--top"></div>
  <h3 class="offroad"><span class="l1">OFF ROAD</span><span class="l2">ADVENTURE</span></h3>
  <p class="offroad-sponsor">SPONSORED BY</p>
  <div class="location-tag location-tag--offroad">
    <span class="cap">Location</span>
    <span class="place">HALE WATER, KENT</span>
  </div>
  <div class="partner-name"><span class="sq"></span>BSK</div>
  <div class="rule rule--bottom"></div>

  <p class="dinner">Followed by dinner<br>and overnight<br>accommodation at</p>
  <p class="venue">Brimwell Manor Hotel &amp;<br>Country Club, Surrey</p>

  <p class="closing">We hope you will be able to join us</p>

  <ul class="contacts">
    <li><svg viewBox="0 0 12 12"><circle cx="6" cy="6" r="5.5" fill="none" stroke="#fff" stroke-width="1.2"/><path d="M.5 6h11M6 .5c-2.4 3-2.4 8 0 11M6 .5c2.4 3 2.4 8 0 11" fill="none" stroke="#fff" stroke-width="1"/></svg>www.prvlumber-example.co.uk</li>
    <li><svg viewBox="0 0 12 12"><rect x=".5" y="2" width="11" height="8" fill="#fff"/><path d="M.5 2l5.5 4.5L11.5 2" fill="none" stroke="#1f2b22" stroke-width="1"/></svg>sales@prvlumber-example.co.uk</li>
    <li><svg viewBox="0 0 12 12"><path d="M2.3.8l2 2.3-1 1.4c.8 1.7 2 2.9 3.7 3.8l1.4-1 2.3 2-1.1 1.9C5.3 11 1 6.7.7 2z"/></svg>+44 (0) 20 7946 0817</li>
  </ul>
</section>

</body>
</html>
```